Website Design for Solar Panel Company

We are working with a company called VoltaryNX.

Some sites to use for content/competitors and inspiration:
https://www.brightmoor.example
https://prod.cld-prod.raylumen.example
https://amberfieldvolt.example
https://www.korvane.example/solarpanels

Thank you for taking the time to consider designing a website for us. We are web developers based in Stockton, CA, USA. Most of our projects go through the same process. Understanding this process may help you win a project with us. We custom-code all of our websites in-house. We don’t have any requirements as to what tools you use for your design, but we prefer Figma files. For any design that we label as four-stars, we send it to the client for review. The client picks the final design they want us to use. Once we complete this process, we will continue to show additional clients all the four-star sites and purchase them later. Your designs will have multiple chances to sell. For better chances of success, we ask that you follow these guidelines.

IMAGES:
If you use any images or icons in the design, we ask that you have a link to the asset so we can purchase the image/icon. Most of the designs we submit do not have the customer’s images on them unless they have some great images. Be creative; show us the feeling you are trying to portray with your image choices. Use any royalty-free site you choose. We subscribe to Quillex and mainly use their images, but we can purchase images outside of Quillex. PLEASE NOTE: we will not submit designs to clients with watermarks on the images.

FONTS:
We ask that you identify the fonts used in the design. This can be done in a message if you want. We typically use Marlowe Fonts and Quillex Fonts.

CONTENT:
We're always open to different content and ideas. We often submit designs with stock images so the client can see our vision. We typically take pictures after the website launch to use their images with our vision. Lorem Ipsum is fine for paragraphs, but we ask that you write the headers in correct English. We want to be able to show the vision and identify the sections of the website.

INSPIRATION:
We typically add a couple of links in the brief of websites we like to help you get started in your design.

REVISIONS:
We do not often ask for revisions of the designs unless we see something in the design that may not appeal to the client. If there are slight changes that we want to make, we do that in the development process.

FEEDBACK:
We rarely give feedback on designs during the design process. We are working on many website projects and do not have the time to provide feedback. We usually respond if your request is well thought out and asks specific questions, but a note asking “feedback, please” usually goes unanswered.

```html
<!DOCTYPE html>
<html lang="en">
<head>
<meta charset="utf-8">
<title>VoltaryNX – Solar Energy</title>
<link href="https://fonts.googleapis.com/css2?family=Orbitron:wght@700&family=Roboto:wght@400;500;700&display=swap" rel="stylesheet">
<style>
:root{
  --green:#1f9a12;
  --green-bright:#43b51f;
  --green-light:#8fdc4a;
  --black:#000;
  --ink:#111;
  --text:#222;
  --white:#fff;
}
*{box-sizing:border-box;margin:0;padding:0}
html,body{width:1200px;height:3957px;overflow:hidden;background:var(--white)}
body{font-family:"Roboto",Arial,sans-serif;color:var(--text);position:relative}
.abs{position:absolute}
.heading{font-family:"Orbitron",Arial,sans-serif;font-weight:700;color:var(--ink);letter-spacing:0.5px}
.divider-dot{position:absolute;width:34px;height:34px;border-radius:50%;background:var(--green-bright)}

/* call-to-action buttons */
.btn{position:absolute;z-index:5;isolation:isolate;display:flex;align-items:center;justify-content:center;color:var(--white);font-weight:700;font-size:16px;text-transform:uppercase;text-decoration:none}
.btn::before{content:"";position:absolute;top:0;bottom:0;left:14px;right:14px;background:var(--green);transform:skewX(25deg);z-index:-1}
.btn::after{content:"";position:absolute;top:0;bottom:0;left:0;right:0;border-left:6px solid var(--green-light);border-right:6px solid var(--green-light);transform:skewX(25deg);z-index:-2}
.btn span{position:relative;z-index:1}

/* header */
.site-header{position:absolute;left:0;top:0;width:1200px;height:97px;background:var(--white);z-index:2}
.brand{position:absolute;left:110px;top:22px;font-weight:700;font-size:46px;color:var(--ink);display:flex;align-items:center;gap:12px}
.brand-mark{width:22px;height:22px;border-radius:50%;background:var(--green-bright)}
.phone{position:absolute;left:726px;top:8px;display:flex;align-items:center;gap:8px;font-size:16px;font-weight:500;color:var(--ink)}
.icon-circle{width:40px;height:40px;border-radius:50%;background:var(--green);display:flex;align-items:center;justify-content:center}
.main-nav a{position:absolute;top:63px;font-size:16px;font-weight:500;color:var(--ink);text-decoration:none}
.main-nav a.active{color:var(--green)}

/* hero */
.hero{position:absolute;left:0;top:97px;width:1200px;height:667px;clip-path:path('M0 0H1200V528Q600 800 0 528Z');background:linear-gradient(180deg,#5c7798 0%,#8aa0b8 25%,#4a5560 50%,#3b3a3c 75%,#2f4a2c 100%)}
.hero-title{position:absolute;width:1200px;text-align:center;color:var(--white)}

/* about */
.about-photo{position:absolute;left:112px;top:860px;width:464px;height:464px;border-radius:50%;background:linear-gradient(160deg,#9fc3e4,#5a86bf 45%,#2c4f8c 80%,#1f3560)}
.about-text{position:absolute;left:642px;top:971px;width:445px;font-size:15.4px;line-height:28.3px;color:var(--text)}

/* services */
.svc-card{position:absolute;border-radius:8px;overflow:hidden}
.svc-card .label{position:absolute;left:0;right:0;bottom:26px;text-align:center;color:var(--white);font-weight:700;font-size:15px;text-transform:uppercase}
.arrow{position:absolute;top:1508px}

/* partners */
.partner-badge{position:absolute;border-radius:10px}

/* testimonials */
.testimonials{position:absolute;left:0;top:2537px;width:1200px;height:484px;background:linear-gradient(135deg,#2f9a1c,#43b51f 50%,#2b8f18)}
.quote{position:absolute;left:195px;top:2722px;width:478px;font-size:15px;line-height:28.3px;color:var(--white)}
.client-photo{position:absolute;left:727px;top:2701px;width:246px;height:246px;border-radius:50%;background:linear-gradient(180deg,#dfe6ec,#9fb2c6 60%,#3e5f86)}
.quote-footer{position:absolute;left:195px;top:2915px;display:flex;align-items:center;gap:10px}
.client-name{color:#fff;font-family:"Orbitron",Arial,sans-serif;font-weight:700;font-size:19px;display:flex;align-items:center;gap:6px;margin-right:8px;white-space:nowrap}
.client-name::before{content:"";display:inline-block;width:28px;height:3px;background:#fff}
.nav-dot{width:34px;height:34px;border-radius:50%;display:flex;align-items:center;justify-content:center;flex:none}

/* video + footer */
.video-frame{position:absolute;left:121px;top:3119px;width:958px;height:430px;border:5px solid var(--green-bright);border-radius:30px;overflow:hidden;background:linear-gradient(180deg,#485566 0%,#c98a3c 30%,#f3b64a 36%,#4f5a3f 45%,#324257 75%,#1c2940 100%)}
.play{position:absolute;left:547px;top:3282px;width:104px;height:104px;border-radius:50%;background:rgba(255,255,255,.6);display:flex;align-items:center;justify-content:center}
.play div{width:60px;height:60px;border-radius:50%;background:#fff;display:flex;align-items:center;justify-content:center}
.footer-col h3{position:absolute;top:3628px;font-size:20px;font-weight:700;color:var(--white)}
.footer-links a{position:absolute;left:363px;font-size:16px;font-weight:500;color:var(--white);text-decoration:none}
.contact-item{position:absolute;left:525px;display:flex;align-items:center;gap:12px;font-size:16px;font-weight:500;color:var(--white)}
.contact-item .icon-circle{width:44px;height:44px;background:var(--green-bright)}
.email-input{position:absolute;left:813px;top:3674px;width:275px;height:40px;background:var(--white);border:1px solid #ccc;padding:0 12px;font-size:14px;color:#555;display:flex;align-items:center}
.copyright{position:absolute;left:0;width:1200px;top:3900px;text-align:center;color:var(--white);font-size:14px}
</style>
</head>
<body>

<header class="site-header">
  <div class="brand"><span class="brand-mark"></span>VoltaryNX</div>
  <div class="phone">
    <span class="icon-circle"><svg width="20" height="20" viewBox="0 0 24 24"><path fill="#fff" d="M6.6 10.8a15 15 0 0 0 6.6 6.6l2.2-2.2c.3-.3.7-.4 1-.2 1.1.4 2.3.6 3.6.6.6 0 1 .4 1 1V20c0 .6-.4 1-1 1C10.6 21 3 13.4 3 4c0-.6.4-1 1-1h3.5c.6 0 1 .4 1 1 0 1.3.2 2.5.6 3.6.1.3 0 .7-.2 1z"/></svg></span>
    +1(555)010 0188
  </div>
  <nav class="main-nav">
    <a class="active" style="left:383px">Home</a>
    <a style="left:467px">About Us</a>
    <a style="left:576px">Services</a>
    <a style="left:681px">Testimonials</a>
    <a style="left:817px">Contact Us</a>
  </nav>
  <a class="btn" style="left:953px;top:51px;width:132px;height:40px;font-size:15px"><span>Login &#9679;</span></a>
</header>

<section class="hero" role="img" aria-label="House roof covered with solar panels under a blue sky"></section>
<div class="hero-title" style="top:272px;font-size:25px;font-weight:500">WELCOME TO</div>
<div class="hero-title" style="top:318px;font-size:96px;font-weight:700;line-height:1.1">VoltaryNX</div>
<a class="btn" style="left:522px;top:461px;width:157px;height:41px"><span>Get Started</span></a>

<section class="about">
  <div class="about-photo" role="img" aria-label="Two technicians installing a solar panel on a roof"></div>
  <h2 class="heading abs" style="left:642px;top:858px;font-size:34px">ABOUT US</h2>
  <div class="divider-dot" style="left:643px;top:906px"></div>
  <p class="about-text">Lorem ipsum dolor sit amet, consectetur adipiscing elit, iusmod tempor incididunt ut labore et dolore magna aliqua. uis ccumsan lacus vel facilisis.Lorem ipsum dolor sit amet, consectetur iscing elit, iusmod tempor incididunt ut labore et dolore magna aliqua. ametonsectetur adipiscing elit, iusmod tempor incididunt labore et dolore magna aliqua. uis ccumsan lacus vel facilisis.Lorem ipsum dolor sit amet, consectetur iscing elit, iusmod tempor incididunt ut labore et dolore magna aliqua. uis ccumsan lacus vel facilisis.</p>
  <a class="btn" style="left:647px;top:1238px;width:166px;height:40px"><span>Read More</span></a>
</section>

<section class="services">
  <h2 class="heading abs" style="left:0;width:1200px;text-align:center;top:1418px;font-size:34px">OUR SERVICES</h2>
  <div class="divider-dot" style="left:583px;top:1468px"></div>
  <svg class="arrow" style="left:1096px" width="32" height="32" viewBox="0 0 32 32"><path d="M28 16H5M13 8l-8 8 8 8" fill="none" stroke="#111" stroke-width="2.5"/></svg>
  <svg class="arrow" style="left:1140px" width="32" height="32" viewBox="0 0 32 32"><path d="M4 16h23M19 8l8 8-8 8" fill="none" stroke="#111" stroke-width="2.5"/></svg>
  <div class="svc-card" style="left:0;top:1586px;width:281px;height:411px;background:linear-gradient(180deg,#3d86c9,#6da1cf 30%,#9a4a32 55%,#5a3a2a)" role="img" aria-label="Residential roof with solar panels"><div class="label" style="text-align:left;left:78px;bottom:20px">Residential</div></div>
  <div class="svc-card" style="left:289px;top:1550px;width:301px;height:412px;background:linear-gradient(180deg,#8a7a5e,#5b7fb0 35%,#3a5f96 55%,#c9c9c9 70%,#6d6a5a)" role="img" aria-label="Commercial building with rooftop solar array"><div class="label">Commercial</div></div>
  <div class="svc-card" style="left:599px;top:1584px;width:301px;height:413px;background:linear-gradient(180deg,#35668c,#7a5244 40%,#9b4b34 70%,#6a3426)" role="img" aria-label="Two workers carrying a solar panel on a tiled roof"><div class="label">Solar Installation</div></div>
  <div class="svc-card" style="left:908px;top:1550px;width:300px;height:412px;background:linear-gradient(200deg,#f1e2b8,#5c7fae 35%,#2d4f87 70%,#1d3563)" role="img" aria-label="Technicians maintaining a large solar panel field"><div class="label">Solar Maintanence</div></div>
</section>

<section class="partners">
  <h2 class="heading abs" style="left:0;width:1200px;text-align:center;top:2088px;font-size:34px">OUR PARTNERS</h2>
  <div class="divider-dot" style="left:588px;top:2138px"></div>
  <div class="partner-badge" style="left:172px;top:2224px;width:130px;height:140px;background:#e7eef6"></div>
  <div class="partner-badge" style="left:402px;top:2232px;width:104px;height:130px;background:#e7eef6"></div>
  <div class="partner-badge" style="left:592px;top:2226px;width:148px;height:138px;background:#e7eef6"></div>
  <div class="partner-badge" style="left:804px;top:2228px;width:212px;height:138px;background:#e7eef6"></div>
  <a class="btn" style="left:516px;top:2401px;width:168px;height:39px"><span>View More</span></a>
</section>

<section class="testimonials"></section>
<h2 class="heading abs" style="left:0;width:1200px;text-align:center;top:2588px;font-size:32px;color:#fff">CLIENT TESTIMONIALS</h2>
<div class="divider-dot" style="left:583px;top:2638px;background:#fff"></div>
<p class="quote">Lorem ipsum dolor sit amet, consectetur adipiscing elit, sed usmodse tempor incididunt ut labore et dolore magna aliqua. trices gravidaisus commodo viverra maecenas accumsan lacus vel acilisis.Loremipsum dolor sit amet, consectetur adipiscing elit, sed usmodse ididunt abore et dolore magna aliqua. sumuspendisse ultrices gravida. Risus modo viverra maecenas accumsan lacus vel facilisis.</p>
<div class="quote-footer">
  <span class="client-name">DARREN</span>
  <span class="nav-dot" style="background:rgba(255,255,255,.55)"><svg width="14" height="14" viewBox="0 0 14 14"><path d="M9 2L4 7l5 5" fill="none" stroke="#1f9a12" stroke-width="2.5"/></svg></span>
  <span class="nav-dot" style="background:#fff"><svg width="14" height="14" viewBox="0 0 14 14"><path d="M5 2l5 5-5 5" fill="none" stroke="#111" stroke-width="2.5"/></svg></span>
</div>
<svg class="abs" style="left:697px;top:2671px" width="306" height="306" viewBox="0 0 306 306">
  <circle cx="153" cy="153" r="143" fill="none" stroke="#0d3d08" stroke-width="12" stroke-dasharray="330 900" transform="rotate(160 153 153)"/>
  <circle cx="153" cy="153" r="143" fill="none" stroke="#8fdc4a" stroke-width="12" stroke-dasharray="420 900" transform="rotate(-30 153 153)"/>
  <circle cx="153" cy="153" r="130" fill="none" stroke="#b8ec7a" stroke-width="6" stroke-dasharray="260 900" transform="rotate(20 153 153)"/>
</svg>
<div class="client-photo" role="img" aria-label="Portrait of a smiling client in a checked shirt"></div>

<svg class="abs" style="left:0;top:3380px" width="1200" height="577" viewBox="0 0 1200 577"><path d="M0 110Q600 -160 1200 110V577H0Z" fill="#000"/></svg>
<div class="video-frame" role="img" aria-label="Aerial view of a solar farm at sunset"></div>
<div class="play"><div><svg width="26" height="26" viewBox="0 0 26 26"><circle cx="13" cy="13" r="13" fill="#d71f26"/><path d="M10 7l9 6-9 6z" fill="#fff"/></svg></div></div>

<footer>
  <div class="abs" style="left:110px;top:3650px;font-weight:700;font-size:46px;color:#fff;display:flex;align-items:center;gap:12px"><span class="brand-mark"></span>VoltaryNX</div>
  <div class="footer-col"><h3 style="left:363px">Quick Links</h3><h3 style="left:525px">Contact Us</h3><h3 style="left:813px">Subscribe To Our Newsletter</h3></div>
  <nav class="footer-links">
    <a style="top:3685px">Home</a><a style="top:3724px">About Us</a><a style="top:3762px">Services</a><a style="top:3801px">Testimonials</a><a style="top:3839px">Contact Us</a>
  </nav>
  <div class="contact-item" style="top:3676px"><span class="icon-circle"><svg width="20" height="16" viewBox="0 0 20 16"><rect x="1" y="1" width="18" height="14" rx="2" fill="#fff"/><path d="M1 3l9 6 9-6" fill="none" stroke="#43b51f" stroke-width="2"/></svg></span>info@voltarynx.example</div>
  <div class="contact-item" style="top:3741px"><span class="icon-circle"><svg width="16" height="22" viewBox="0 0 16 22"><path d="M8 0a8 8 0 0 0-8 8c0 6 8 14 8 14s8-8 8-14a8 8 0 0 0-8-8z" fill="#fff"/><circle cx="8" cy="8" r="3" fill="#43b51f"/></svg></span>VoltaryNX, USA</div>
  <div class="contact-item" style="top:3805px"><span class="icon-circle"><svg width="20" height="20" viewBox="0 0 24 24"><path fill="#fff" d="M6.6 10.8a15 15 0 0 0 6.6 6.6l2.2-2.2c.3-.3.7-.4 1-.2 1.1.4 2.3.6 3.6.6.6 0 1 .4 1 1V20c0 .6-.4 1-1 1C10.6 21 3 13.4 3 4c0-.6.4-1 1-1h3.5c.6 0 1 .4 1 1 0 1.3.2 2.5.6 3.6.1.3 0 .7-.2 1z"/></svg></span>+1(555)010 0188</div>
  <div class="email-input">Email</div>
  <a class="btn" style="left:813px;top:3731px;width:166px;height:37px;font-size:15px"><span>Submit Now</span></a>
  <p class="copyright">Copyright © 2024 VoltaryNX. | All Rights Reserved</p>
</footer>

</body>
</html>
```